Visitenkarten für Containerhandel
BROV
alles tip top wie bestellt so wurde geliefert!
Zielgruppe
Wir handeln mit See und Lagercontainer
Aufgabenstellung
evtl. Das Seecontainer Designe integrieren
Angaben auf der Karte;
//Frimenangaben//
TORVELMARK AG
Ribelweg 27
CH - 5312 Lindwil
sales@torvelmark.ch
//Personenangaben//
Lukas Brenni
Leiter Verkauf

```html
<!DOCTYPE html>
<html lang="de">
<head>
<meta charset="utf-8">
<title>TORVELMARK AG – Visitenkarten</title>
<link rel="stylesheet" href="https://fonts.googleapis.com/css2?family=Jost:wght@400;700&display=swap">
<style>
  :root {
    --backdrop: #c3dff2;
    --navy: #1b2a63;
    --paper: #ffffff;
    --ink: #111111;
    --card-shadow: 0 18px 40px rgba(30, 60, 100, 0.22);
  }
  html, body {
    margin: 0;
    padding: 0;
    width: 1200px;
    height: 873px;
    overflow: hidden;
    background: var(--backdrop);
    font-family: "Jost", sans-serif;
  }
  .sheet {
    position: relative;
    width: 1200px;
    height: 873px;
  }
  .card {
    position: absolute;
    top: 268px;
    width: 520px;
    height: 336px;
    box-shadow: var(--card-shadow);
    overflow: hidden;
  }
  .card--front {
    left: 50px;
    background: var(--paper);
    color: var(--ink);
  }
  .card--back {
    left: 630px;
    background: var(--navy);
    display: flex;
    align-items: center;
    justify-content: center;
  }
  .front__tab {
    position: absolute;
    left: 34px;
    top: 0;
    width: 150px;
    height: 64px;
    background: var(--navy);
  }
  .wordmark {
    font-family: "Jost", sans-serif;
    font-weight: 700;
    letter-spacing: 0.02em;
    line-height: 1;
    margin: 0;
  }
  .front__wordmark {
    position: absolute;
    left: 38px;
    top: 74px;
    font-size: 34px;
    color: var(--ink);
  }
  .front__person {
    position: absolute;
    left: 38px;
    top: 128px;
  }
  .person__name {
    margin: 0;
    font-weight: 700;
    font-size: 21px;
    line-height: 1.1;
  }
  .person__role {
    margin: 2px 0 0;
    font-weight: 400;
    font-size: 14px;
  }
  .front__contact {
    position: absolute;
    left: 250px;
    top: 186px;
    font-size: 15px;
    line-height: 1.3;
    font-style: normal;
  }
  .contact__line {
    margin: 0;
  }
  .contact__gap {
    height: 12px;
  }
  .back__wordmark {
    font-size: 58px;
    color: var(--paper);
  }
</style>
</head>
<body>
  <main class="sheet">
    <section class="card card--front" aria-label="Visitenkarte Vorderseite">
      <div class="front__tab"></div>
      <p class="wordmark front__wordmark">TORVELMARK</p>
      <div class="front__person">
        <p class="person__name">Lukas Brenni</p>
        <p class="person__role">Leiter Verkauf</p>
      </div>
      <address class="front__contact">
        <p class="contact__line">+41 62 734 18 06</p>
        <p class="contact__line">sales@torvelmark.ch</p>
        <div class="contact__gap"></div>
        <p class="contact__line">TORVELMARK AG</p>
        <p class="contact__line">Ribelweg 27</p>
        <p class="contact__line">CH - 5312 Lindwil</p>
      </address>
    </section>
    <section class="card card--back" aria-label="Visitenkarte Rückseite">
      <p class="wordmark back__wordmark">TORVELMARK</p>
    </section>
  </main>
</body>
</html>
```